Pagecraft Keepsakes needs a book cover for sample to share with clients.

We are a start up company that is presently putting together all the tools to call on community groups. We write memoirs for seniors in order to help them put their "ordinary lives...extraordinary legacies" on paper in an 8 x 10 hardcover book that will be 120 to 200 pages including text and photos.These are meant to be cherished by family for generations to come!
We want a front cover that has the attached photo of the woman at her writing desk (with the words cropped out). The cover needs to have Pagecraft Keepsakes and the catchphrase "Every life legacy is a gift to be treasured by the next generation".
We are also attaching our new logo which should be somewhere in the design.
We want a back cover that will have the attached photo of the couple on the beach (preferably with a lightly enhanced sunset) with the catchphrase "When a genealogy doesn't say enough".
The spine just needs to have Pagecraft Keepsakes.com and the logo (if it will fit). The 120 page book is only a 1/2 inch spine. The 200 page would be 3/4 to 1 inch.

Target Market(s)

Seniors

Industry/Entity Type

It Company

Colors
faa54b
f59195
fabb94
fee18a
fbca95

Requirements
Must have
• Attached photos

```html
<!DOCTYPE html>
<html lang="en">
<head>
<meta charset="utf-8">
<title>Pagecraft Keepsakes – Book Cover</title>
<link rel="stylesheet" href="https://fonts.googleapis.com/css2?family=Arimo:wght@400;700&family=Dancing+Script:wght@600&display=swap">
<style>
  :root {
    --page-bg: #ffffff;
    --spine-pink: #f59195;
    --spine-band: #ffffff;
    --title-pink: #f59195;
    --title-shadow: #4a2412;
    --quote-gold: #fee18a;
    --photo-deep: #2a140b;
    --photo-mid: #6b3820;
    --photo-warm: #b5663a;
    --photo-glow: #faa54b;
    --badge-bg: #fdf8f1;
    --badge-ink: #7a5a3a;
  }
  * { margin: 0; padding: 0; box-sizing: border-box; }
  html, body {
    width: 1200px; height: 989px; overflow: hidden;
    background: var(--page-bg);
  }
  .book {
    position: absolute; left: 221px; top: 64px;
    width: 758px; height: 860px;
    display: flex;
    box-shadow: 0 10px 30px rgba(0,0,0,0.12);
  }
  .spine {
    position: relative; width: 70px; height: 100%;
    background: var(--spine-pink);
  }
  .spine-band {
    position: absolute; left: 14px; top: 150px;
    width: 42px; height: 560px;
    background: var(--spine-band);
    display: flex; align-items: center; justify-content: center;
  }
  .spine-title {
    writing-mode: vertical-rl;
    font-family: "Arimo", sans-serif; font-size: 30px; letter-spacing: 1px;
    color: var(--spine-pink); white-space: nowrap;
  }
  .spine-mark {
    position: absolute; left: 17px; width: 36px; height: 100px;
    border: 1px solid rgba(255,255,255,0.7);
    display: flex; align-items: center; justify-content: center;
  }
  .spine-mark--top { top: 30px; }
  .spine-mark--bottom { bottom: 30px; }
  .spine-mark span {
    writing-mode: vertical-rl;
    font-family: "Arimo", sans-serif; font-size: 8px;
    color: rgba(255,255,255,0.85); white-space: nowrap;
  }
  .front {
    position: relative; width: 688px; height: 100%; overflow: hidden;
  }
  .cover-photo {
    position: absolute; inset: 0;
    background:
      radial-gradient(circle at 24% 66%, var(--photo-glow) 0%, rgba(250,165,75,0.35) 12%, transparent 32%),
      radial-gradient(ellipse at 85% 15%, #b57a5a 0%, transparent 55%),
      linear-gradient(160deg, var(--photo-mid) 0%, var(--photo-deep) 45%, var(--photo-warm) 75%, var(--photo-deep) 100%);
  }
  .cover-quote {
    position: absolute; left: 150px; top: 150px; width: 460px;
    font-family: "Dancing Script", cursive; font-size: 27px; line-height: 1.15;
    color: var(--quote-gold); text-align: center;
    transform: rotate(-22deg);
  }
  .cover-title {
    position: absolute; left: 0; right: 0; top: 500px;
    text-align: center;
    font-family: "Arimo", sans-serif; font-weight: 700;
    color: var(--title-pink);
    text-shadow: 3px 3px 0 var(--title-shadow);
  }
  .cover-title .word { display: block; font-size: 56px; line-height: 1; letter-spacing: 1px; }
  .cover-title .joiner {
    display: block; font-family: "Dancing Script", cursive; font-weight: 600;
    font-size: 34px; line-height: 1.2; text-shadow: none;
  }
  .cover-badge {
    position: absolute; left: 284px; top: 745px;
    width: 120px; height: 60px;
    background: var(--badge-bg);
    display: flex; align-items: center; justify-content: center;
    font-family: "Arimo", sans-serif; font-size: 11px; color: var(--badge-ink);
    text-align: center; line-height: 1.2;
  }
</style>
</head>
<body>
  <div class="book">
    <aside class="spine">
      <div class="spine-mark spine-mark--top"><span>Pagecraft Keepsakes</span></div>
      <div class="spine-band"><span class="spine-title">pagecraft keepsakes.com</span></div>
      <div class="spine-mark spine-mark--bottom"><span>Pagecraft Keepsakes</span></div>
    </aside>
    <section class="front">
      <div class="cover-photo" role="img" aria-label="Photo of an elderly woman in a lace shawl writing at a wooden desk lit by an oil lamp"></div>
      <p class="cover-quote">“ Every life legacy is a gift to be treasured by the next generation ”</p>
      <h1 class="cover-title">
        <span class="word">PAGECRAFT</span>
        <span class="joiner">by</span>
        <span class="word">KEEPSAKES</span>
      </h1>
      <div class="cover-badge">Pagecraft<br>Keepsakes</div>
    </section>
  </div>
</body>
</html>
```